Snapframe Party Rentals New Business Card*

Need a business card designed for a Photo Booth Hire company.Must look very professional and colorful.A new creative logo would be a bonus. Our current logo is attached on here.

Contact Information for Business Card

Business Name: SNAPFRAME PARTY RENTALS
Contact Person: MARCUS OKAFOR
Mobile: 0491862035
Email: INFO@SNAPFRAMEPARTY.EXAMPLE
Website: WWW.SNAPFRAMEPARTY.EXAMPLE
Facebook: WWW.SOCIALNET.EXAMPLE/SNAPFRAME.PARTY.RENT

Font styles to use
Serif
Sans Serif
Script

Colors

Designer to choose colors to be used in the design.

Requirements
Must have
• Bonus if the colors match our website.

```html
<!DOCTYPE html>
<html lang="en">
<head>
<meta charset="utf-8">
<title>Snapframe Party Rentals – Business Card</title>
<link href="https://fonts.googleapis.com/css2?family=Barlow:wght@700&family=Montserrat:wght@500;700&display=swap" rel="stylesheet">
<style>
  :root {
    --stage: #2b2b2e;
    --ink: #0b0b0b;
    --paper: #ffffff;
    --faint: #e9e9e9;
    --text-dark: #151515;
    --text-light: #ffffff;
  }
  * { margin: 0; padding: 0; box-sizing: border-box; }
  html, body { width: 1200px; height: 800px; overflow: hidden; }
  body {
    background: var(--stage);
    position: relative;
    font-family: "Montserrat", sans-serif;
  }
  .card {
    position: absolute;
    top: 245px;
    width: 540px;
    height: 310px;
    overflow: hidden;
    box-shadow: 0 10px 30px rgba(0,0,0,.45);
  }

  /* Front */
  .card--front { left: 40px; background: var(--ink); }
  .brand {
    position: absolute;
    left: 50%; top: 50%;
    transform: translate(-50%, -50%);
    display: flex; flex-direction: column; align-items: center;
    color: var(--text-light);
  }
  .brand__mark {
    width: 70px; height: 70px; border-radius: 50%;
    background: var(--paper);
    margin-bottom: 16px;
  }
  .brand__name {
    font-family: "Barlow", sans-serif;
    font-weight: 700;
    font-size: 25px;
    line-height: 1.02;
    letter-spacing: .5px;
    text-align: center;
    text-transform: uppercase;
  }
  .brand__url {
    font-family: "Barlow", sans-serif;
    font-weight: 700;
    font-size: 11px;
    letter-spacing: .4px;
    margin-top: 5px;
  }

  /* Back */
  .card--back { left: 620px; background: var(--paper); }
  .back__band {
    position: absolute; left: 0; top: 0; bottom: 0;
    width: 122px;
    background: var(--ink);
    color: var(--text-light);
    display: flex; align-items: center; justify-content: center;
  }
  .band__text {
    transform: rotate(90deg);
    white-space: nowrap;
    font-family: "Barlow", sans-serif;
    font-weight: 700;
    text-align: left;
  }
  .band__name { font-size: 21px; line-height: 1.02; text-transform: uppercase; }
  .band__url { font-size: 10px; margin-top: 4px; letter-spacing: .3px; }
  .back__decor {
    position: absolute;
    right: -40px; top: -70px;
    width: 260px; height: 260px;
    border-radius: 50%;
    background: var(--faint);
  }
  .contact {
    position: absolute;
    left: 148px; bottom: 34px;
    color: var(--text-dark);
  }
  .contact__name {
    font-weight: 700;
    font-size: 19px;
    letter-spacing: .8px;
    margin-bottom: 14px;
  }
  .contact__list { list-style: none; }
  .contact__item {
    display: flex; align-items: center; gap: 9px;
    font-size: 11.5px; font-weight: 500;
    letter-spacing: .3px;
    line-height: 1.75;
  }
  .contact__icon { width: 12px; height: 12px; flex: none; }
</style>
</head>
<body>

<section class="card card--front" aria-label="Card front">
  <div class="brand">
    <div class="brand__mark"></div>
    <div class="brand__name">Snapframe<br>Party Rentals</div>
    <div class="brand__url">WWW.SNAPFRAMEPARTY.EXAMPLE</div>
  </div>
</section>

<section class="card card--back" aria-label="Card back">
  <div class="back__decor"></div>
  <div class="back__band">
    <div class="band__text">
      <div class="band__name">Snapframe<br>Party Rentals</div>
      <div class="band__url">WWW.SNAPFRAMEPARTY.EXAMPLE</div>
    </div>
  </div>

  <div class="contact">
    <h1 class="contact__name">MARCUS OKAFOR</h1>
    <ul class="contact__list">
      <li class="contact__item">
        <svg class="contact__icon" viewBox="0 0 12 12"><rect x="1.5" y="1.5" width="9" height="9" rx="1.5" fill="none" stroke="#151515" stroke-width="1.3"/></svg>
        0491862035
      </li>
      <li class="contact__item">
        <svg class="contact__icon" viewBox="0 0 12 12"><rect x="0.5" y="2" width="11" height="8" fill="#151515"/><path d="M1 2.5 L6 6.5 L11 2.5" fill="none" stroke="#fff" stroke-width="1"/></svg>
        INFO@SNAPFRAMEPARTY.EXAMPLE
      </li>
      <li class="contact__item">
        <svg class="contact__icon" viewBox="0 0 12 12"><circle cx="6" cy="6" r="5.5" fill="#151515"/><path d="M0.5 6 H11.5 M6 0.5 C3 3.5 3 8.5 6 11.5 M6 0.5 C9 3.5 9 8.5 6 11.5" fill="none" stroke="#fff" stroke-width=".8"/></svg>
        WWW.SNAPFRAMEPARTY.EXAMPLE
      </li>
      <li class="contact__item">
        <svg class="contact__icon" viewBox="0 0 12 12"><circle cx="6" cy="6" r="4.5" fill="#151515"/></svg>
        WWW.SOCIALNET.EXAMPLE/SNAPFRAME.PARTY.RENT
      </li>
    </ul>
  </div>
</section>

</body>
</html>
```